Sophrologist needs a cool signage at door entrance

I need signage for dr in sophrology based in Belgium (french speaking). The signed should capture the name the "Mireille Vantoorn" - "Naturopathe-Sophrologue-Reiki" and a catchphrase = (Healthy way of life)
« Fais du bien à ton corps, pour que ton âme ait envie d’y rester »
Requirements
Must have
- Hey,
Thats the instagram account for some inspiration www.instagram.com/mireille_serene_wellbeing
Light colors, green, blue
Healthy way of life
Size is 45cm wide on 30 cm high
The signage will be placed in front off woof pannel

```html
<!DOCTYPE html>
<html lang="fr">
<head>
<meta charset="utf-8">
<title>Mireille Vantoorn – Enseigne</title>
<link rel="stylesheet" href="https://fonts.googleapis.com/css2?family=Gloock&display=swap">
<style>
  :root {
    --stage: #e8e8ea;
    --card: #ffffff;
    --blush-faint: #fdf5f8;
    --blush-light: #fae6ee;
    --blush-mid: #f5aacb;
    --blush-deep: #ef8ab5;
    --rose-text: #ee86b3;
    --ink: #4a4a4c;
  }
  html, body {
    margin: 0;
    padding: 0;
    width: 1200px;
    height: 869px;
    overflow: hidden;
    background: var(--stage);
  }
  .sign {
    position: absolute;
    left: 0;
    top: 34px;
    width: 1200px;
    height: 800px;
    background: var(--card);
    overflow: hidden;
    font-family: "Gloock", "Times New Roman", serif;
  }
  .sign__backdrop {
    position: absolute;
    inset: 0;
    background:
      radial-gradient(ellipse 38% 75% at 50% 45%, var(--blush-light) 0%, var(--blush-light) 60%, transparent 61%),
      radial-gradient(ellipse 75% 70% at 50% 70%, var(--blush-faint) 0%, var(--blush-faint) 70%, transparent 71%);
  }
  .sign__flower {
    position: absolute;
    left: 0;
    right: 0;
    bottom: 0;
    height: 310px;
    background: linear-gradient(180deg, rgba(245,170,203,0) 0%, var(--blush-mid) 45%, var(--blush-deep) 100%);
  }
  .sign__header {
    position: absolute;
    top: 168px;
    left: 0;
    right: 0;
    text-align: center;
    color: var(--rose-text);
    letter-spacing: -1px;
  }
  .sign__name,
  .sign__title {
    margin: 0;
    font-size: 58px;
    line-height: 58px;
    font-weight: 400;
  }
  .sign__divider {
    position: absolute;
    top: 316px;
    left: 54px;
    width: 1090px;
    height: 6px;
    background: linear-gradient(90deg, #ffffff 0%, var(--rose-text) 50%, #ffffff 100%);
  }
  .sign__motto {
    position: absolute;
    top: 338px;
    left: 0;
    right: 0;
    margin: 0;
    text-align: center;
    color: var(--ink);
    font-size: 72px;
    line-height: 70px;
    font-weight: 400;
    letter-spacing: -1.5px;
  }
</style>
</head>
<body>
  <main class="sign">
    <div class="sign__backdrop" role="img" aria-label="Grands pétales de lotus rose pâle en arrière-plan"></div>
    <div class="sign__flower" role="img" aria-label="Fleur de lotus rose stylisée en bas de l’enseigne"></div>

    <header class="sign__header">
      <h1 class="sign__name">Mireille Vantoorn</h1>
      <p class="sign__title">Naturopathe-Sophrologue-Reiki</p>
    </header>

    <div class="sign__divider"></div>

    <p class="sign__motto">Fais du bien à ton corps, pour<br>que ton âme ait envie d’y rester</p>
  </main>
</body>
</html>
```